Classic/Royal 5 Items Black coloured Stationery Design

Hello,
I'm looking for an Elegant Stationery set consists of 5 items as the following,
1- Letterhead
2- Business Card
3- Invoice
4- CD/DVD with their Envelope Design
5- Envelope
To let the project move ahead easily, I've included a folder consists many designs I liked from various design sites and it consists of,
1- Business card
2- Corporate Identity
3- Invoice
4- Miscellanies
Inside the first three folders, you will find a folder named "Recommended", it contains designs that I like so much and hoping to have a design like them.
The "Miscellanies" folder got some designs for Inspiration.
I'm waiting for some greats designs, a joomla template designer is a bonus for me as I will need him to design the website layer soon.
Due to upload problems at ArtHarbor, I've uploaded the folder in a .rar archive at multiple site and here is the link http://filevanta.example/QZTRLPNB .
Thank you
Update :- You can use this alternative download link from my Nimbox drive to download the designs
https://share.cloudvessel.example/file/d/7Hq2pLx9w4t6KmZr83VnbYsQ5eJd
Business

```html
<!DOCTYPE html>
<html lang="en">
<head>
<meta charset="utf-8">
<title>Crestmere Stationery Set</title>
<link href="https://fonts.googleapis.com/css2?family=Open+Sans:wght@400;600;700&display=swap" rel="stylesheet">
<style>
:root{
  --backdrop:#e6e4e1;
  --paper:#fbfbfb;
  --paper-fade:#e9e9ea;
  --ink:#1c1c1c;
  --ink-soft:#6d6d6d;
  --brand-grey:#8a8a8a;
  --dark:#2b2b2b;
  --dark-deep:#151515;
  --table-head:#4a4a4a;
  --row-tint:#e3ecec;
  --line:#b9b9b9;
}
*{margin:0;padding:0;box-sizing:border-box}
html,body{width:1200px;height:711px;overflow:hidden}
body{background:var(--backdrop);font-family:"Open Sans",Arial,sans-serif;color:var(--ink);position:relative}
.item{position:absolute;box-shadow:0 2px 6px rgba(0,0,0,.25)}
.brand{font-weight:600;color:var(--brand-grey);line-height:1;display:flex;align-items:center;gap:4px}
.brand .mark{width:9px;height:9px;border:1px solid var(--brand-grey)}
.brand-tag{font-size:5px;color:var(--brand-grey);margin-top:2px}

/* business cards */
.card{top:173px;width:96px;height:62px;background:linear-gradient(135deg,var(--dark),var(--dark-deep));display:flex;flex-direction:column;align-items:center;justify-content:center}
.card .brand{color:#e8e8e8;font-size:9px}
.card .brand .mark{border-color:#e8e8e8}
.card .brand-tag{color:#bdbdbd;font-size:4px}
.card-a{left:370px}.card-b{left:476px}

/* sheets */
.sheet{top:257px;width:246px;height:330px;background:linear-gradient(180deg,var(--paper) 55%,var(--paper-fade));padding:10px 12px;font-size:4.5px}
.sheet::after{content:"";position:absolute;left:0;right:0;bottom:0;height:5px;background:var(--dark)}
.invoice{left:139px}.letterhead{left:411px}
.sheet-head{display:flex;justify-content:space-between;height:50px}
.sheet .brand{font-size:11px}
.sender{display:flex;gap:6px;font-size:4.5px;line-height:1.5}
.sender .name{font-size:7px;font-weight:700;line-height:1}
.sender .contact{border-left:1px solid var(--line);padding-left:5px}
.muted{color:var(--ink-soft)}
.client{margin-top:22px;line-height:1.45;color:var(--ink-soft);position:relative}
.invoice-title{position:absolute;right:0;top:0;text-align:right}
.invoice-title .word{font-size:11px;color:var(--ink-soft);margin-top:12px}
.total{font-size:9px;font-weight:700;color:var(--ink-soft);margin-top:2px}
.items{width:100%;border-collapse:collapse;margin-top:8px;font-size:3.6px}
.items th{background:var(--table-head);color:#fff;text-align:left;padding:2px 3px;font-weight:600}
.items td{padding:3px;color:var(--ink-soft)}
.items tr:nth-child(even) td{background:var(--row-tint)}
.sum{margin:8px 0 0 auto;width:88px;border-collapse:collapse;font-size:3.6px}
.sum th{background:var(--table-head);color:#fff;padding:2px 3px;text-align:left}
.sum td{padding:3px;color:var(--ink-soft);border-bottom:1px solid var(--line)}
.terms{margin-top:20px;line-height:1.5;color:var(--ink-soft);width:190px}
.terms b{color:var(--ink);display:block}
.letter{margin-top:28px;font-size:4.6px;line-height:1.45;font-weight:600}
.letter p{margin-bottom:5px}

/* cd sleeve and disc */
.sleeve{left:678px;top:237px;width:184px;height:182px;background:linear-gradient(135deg,#3a3a3a,var(--dark-deep));display:flex;flex-direction:column;align-items:center;justify-content:center;overflow:hidden}
.sleeve::before{content:"";position:absolute;right:-10px;top:70px;width:30px;height:40px;border-radius:50%;background:var(--backdrop)}
.sleeve .brand,.disc .brand{color:#eee;font-size:12px}
.sleeve .brand .mark,.disc .brand .mark{border-color:#eee}
.sleeve .brand-tag,.disc .brand-tag{color:#bbb}
.disc{left:877px;top:240px;width:178px;height:178px;border-radius:50%;background:radial-gradient(circle,#555 0 14%,transparent 14%),radial-gradient(circle,#3b3b3b,var(--dark-deep));border:5px solid #f2f2f2;display:flex;flex-direction:column;align-items:center;padding-top:28px}
.disc .hole{position:absolute;left:50%;top:50%;width:28px;height:28px;margin:-14px;border-radius:50%;background:var(--backdrop);border:5px solid #ddd}
.disc .brand{font-size:9px}

/* envelope */
.envelope{left:688px;top:446px;width:316px;height:142px;background:linear-gradient(180deg,#fff 60%,var(--paper-fade));padding:12px 14px}
.envelope::after{content:"";position:absolute;left:0;right:0;bottom:0;height:5px;background:var(--dark)}
.envelope .brand{font-size:10px}
</style>
</head>
<body>

<div class="item card card-a"><div class="brand"><span class="mark"></span>Crestmere</div><div class="brand-tag">Hotels and General Supplies</div></div>
<div class="item card card-b"><div class="brand"><span class="mark"></span>Crestmere</div><div class="brand-tag">Hotels and General Supplies</div></div>

<section class="item sheet invoice">
  <header class="sheet-head">
    <div><div class="brand"><span class="mark"></span>Crestmere</div><div class="brand-tag">Hotels and General Supplies</div></div>
    <div class="sender">
      <div><div class="name">Name</div>Title: ___________<br>Address: ___________</div>
      <div class="contact"><br>Phone: ___________<br>Email: ___________</div>
    </div>
  </header>
  <div class="client">
    To:<br>Client Name<br>Client Address Line 1<br>Address Line 2<br>City, Province<br>Country
    <div class="invoice-title"><span>Issued 02 Aug 2011</span><br><span>Invoice # 0045</span><div class="word">Invoice</div><span>Project Name Here</span></div>
    <div style="margin-top:6px">Invoice Total</div>
    <div class="total">$2,500.00</div>
    <div style="margin-top:4px">Due by: 30 Sep 2011</div>
  </div>
  <table class="items">
    <tr><th>Item Description</th><th>Qty</th><th>Unit Price</th><th>VAT</th><th>Total</th></tr>
    <tr><td>Website Design</td><td>1</td><td>$2,000</td><td>$0</td><td>$2,000</td></tr>
    <tr><td>Domain Registration</td><td>1</td><td>$50</td><td>$0</td><td>$50</td></tr>
    <tr><td>1 Year Webhosting</td><td>1</td><td>$50</td><td>$0</td><td>$50</td></tr>
    <tr><td>E-Marketing &amp; Strategy Training</td><td>4</td><td>$100</td><td>$0</td><td>$400</td></tr>
  </table>
  <table class="sum">
    <tr><th>Sub Total</th><th>VAT</th><th>Total Due</th></tr>
    <tr><td>$2,500</td><td>$0</td><td>$2,500</td></tr>
  </table>
  <div class="terms"><b>Terms &amp; Conditions of Invoice</b>Payment is due within thirty days of the invoice date. Late payments may carry a small monthly fee. Thank you for your business.</div>
</section>

<section class="item sheet letterhead">
  <header class="sheet-head">
    <div><div class="brand"><span class="mark"></span>Crestmere</div><div class="brand-tag">Hotels and General Supplies</div></div>
    <div class="sender">
      <div><div class="name">Name</div>Title: ___________<br>Address: ___________</div>
      <div class="contact"><br>Phone: ___________<br>Email: ___________</div>
    </div>
  </header>
  <div class="letter">
    <p>412 Alder Crest Road<br>Los Angeles, CA 90001.</p>
    <p>January 20th, 2011</p>
    <p>Mr. Harlow<br>President, Harlow Youth Center<br>87 Quarry Lane<br>New York, NY 10027</p>
    <p>Dear Mr. Harlow,</p>
    <p>In the first paragraph, one needs to give a brief introduction of oneself. One should also give reference to the purpose of the letter in brief.<br>The second paragraph needs to give the details of the letter and its need. This paragraph is mostly longer than the others and plays the main role in the letter. Keep the sentences short and to the point. Avoid using complex words and sentences.</p>
    <p style="margin-top:14px">The third and last paragraph is the conclusion of the letter and can be kept short.</p>
    <p>Sincerely,</p>
    <p>(this is where the signature of the writer will be placed)</p>
    <p>Dana Ellery<br>Read more at: http://www.letterguide.example/articles/letter-format.html</p>
  </div>
</section>

<div class="item sleeve"><div class="brand"><span class="mark"></span>Crestmere</div><div class="brand-tag">Hotels and General Supplies</div></div>

<div class="item disc"><div class="brand"><span class="mark"></span>Crestmere</div><div class="brand-tag">Hotels and General Supplies</div><span class="hole"></span></div>

<div class="item envelope"><div class="brand"><span class="mark"></span>Crestmere</div><div class="brand-tag">Hotels and General Supplies</div></div>

</body>
</html>
```